General Contractors need a new Crisp updated Card Design

We need a new business card design for our company of 25 years based in Toronto call Holvaster Building Inc. : Our goal is to be the leading commercial contractors in Toronto by providing exceptional value to our clients. We work very hard to deliver professional, quality, service in conjunction with consistent price competitiveness to all of our clients on every single project.

Target Market(s)

Design & Build Clients

Industry/Entity Type

Construction Company

Contact Information for Business Card

Address:
18 North Tamlin Glen Road, Unit 57, Marbrook Vale, ON, K7T 2R9
Office: 905-218-5937

Holvasters Logo
Employee Job Description
Employee Cell Phone #
Employee Email
www.holvaster-example.com

Colors

Designer to choose colors to be used in the design.

Requirements
Must have
• Quote Company Saying:
• "Professional. Quality. Service."
Nice to have
• New Crisp up to date look. simple & fresh ( Not to Busy)
Should not have
• NO BLUE PRINTS ON THE BUSINESS CARDS

```html
<!DOCTYPE html>
<html lang="en">
<head>
<meta charset="utf-8">
<title>Holvaster Building Inc. – Business Card</title>
<link rel="stylesheet" href="https://fonts.googleapis.com/css2?family=Montserrat:wght@500;600;700&family=EB+Garamond:ital@1&display=swap">
<style>
  :root{
    --green-bright:#2fc60f;
    --green-mid:#11a510;
    --green-deep:#0a6a0a;
    --green-dark:#044d05;
    --paper:#f7f8f6;
    --ink:#1d1d1d;
    --bg:#d9dcdb;
  }
  *{margin:0;padding:0;box-sizing:border-box}
  html,body{width:1200px;height:1107px;overflow:hidden;background:var(--bg)}
  .canvas{position:relative;width:1200px;height:1107px}
  .card{position:absolute;left:160px;width:880px;height:503px;overflow:hidden;box-shadow:0 6px 18px rgba(0,0,0,.18)}
  .card--back{top:34px;background:linear-gradient(200deg,var(--green-mid) 0%,var(--green-deep) 55%,var(--green-dark) 100%)}
  .card--front{top:570px;background:var(--paper)}

  /* back */
  .brand{position:absolute;display:flex;align-items:center;gap:22px}
  .brand__mark{width:74px;height:74px;border:5px solid currentColor}
  .brand__name{font-family:"Montserrat",sans-serif;font-weight:700;letter-spacing:2px;line-height:1.05;text-transform:uppercase}
  .card--back .brand{left:215px;top:150px;color:#fff}
  .card--back .brand__name{font-size:40px}
  .tagline-band{position:absolute;left:0;right:0;top:350px;height:46px;background:rgba(255,255,255,.08);
    display:flex;align-items:center;justify-content:flex-end;padding-right:70px;
    font-family:"Montserrat",sans-serif;font-weight:600;font-size:19px;letter-spacing:2px;color:#fff}
  .tagline-band .sep{margin:0 12px;opacity:.8}
  .back-stripe{position:absolute;left:0;right:0;top:410px;height:18px;background:var(--green-bright)}
  .back-base{position:absolute;left:0;right:0;top:428px;bottom:0;background:var(--green-dark)}

  /* front */
  .front-topbar{position:absolute;left:0;right:0;top:0;height:20px;background:var(--green-bright)}
  .person{position:absolute;right:70px;top:60px;text-align:right;font-family:"Montserrat",sans-serif}
  .person__name{font-size:38px;font-weight:700;letter-spacing:4px;color:var(--green-mid)}
  .person__role{font-size:22px;font-weight:500;color:var(--ink);margin-top:4px}
  .person__role span{border-bottom:2px solid var(--green-mid);padding-bottom:2px}
  .divider{position:absolute;left:450px;top:110px;width:2px;height:270px;background:var(--green-mid)}
  .card--front .brand{left:80px;top:190px;color:var(--green-mid);gap:14px}
  .card--front .brand__mark{width:44px;height:44px;border-width:4px}
  .card--front .brand__name{font-size:24px}
  .address{position:absolute;left:80px;top:262px;font-family:"EB Garamond",serif;font-style:italic;font-size:18px;line-height:1.3;color:var(--ink);text-align:center;width:330px}
  .contacts{position:absolute;left:490px;top:170px;list-style:none;font-family:"Montserrat",sans-serif;font-size:20px;color:var(--ink)}
  .contacts li{display:flex;align-items:center;gap:20px;height:52px}
  .icon{width:32px;height:32px;border-radius:50%;background:var(--green-mid);display:flex;align-items:center;justify-content:center;flex:none}
  .icon svg{width:18px;height:18px;fill:none;stroke:#fff;stroke-width:2;stroke-linecap:round;stroke-linejoin:round}
  .web-base{position:absolute;left:540px;right:0;top:396px;height:26px;background:var(--green-dark)}
  .web-band{position:absolute;left:560px;right:0;top:406px;height:38px;background:var(--green-bright);
    display:flex;align-items:center;padding-left:24px;font-family:"Montserrat",sans-serif;font-weight:500;font-size:19px;color:#fff}
  .web-icon{position:absolute;left:490px;top:409px}
  .front-footbar{position:absolute;left:0;top:448px;width:470px;height:26px;background:var(--green-bright)}
  .front-footline{position:absolute;left:0;right:0;bottom:0;height:8px;background:var(--green-mid)}
</style>
</head>
<body>
<main class="canvas">

  <section class="card card--back" aria-label="Card back">
    <div class="brand">
      <div class="brand__mark"></div>
      <div class="brand__name">Holvaster<br>Building Inc.</div>
    </div>
    <div class="tagline-band">PROFESSIONAL<span class="sep">|</span>QUALITY<span class="sep">|</span>SERVICE</div>
    <div class="back-stripe"></div>
    <div class="back-base"></div>
  </section>

  <section class="card card--front" aria-label="Card front">
    <div class="front-topbar"></div>

    <div class="person">
      <div class="person__name">DORIAN PELL</div>
      <div class="person__role">Co-Founder &amp; <span>CEO</span></div>
    </div>

    <div class="divider"></div>

    <div class="brand">
      <div class="brand__mark"></div>
      <div class="brand__name">Holvaster<br>Building Inc.</div>
    </div>
    <p class="address">18 North Tamlin Glen Road, Unit 57,<br>Marbrook Vale, ON, K7T 2R9</p>

    <ul class="contacts">
      <li><span class="icon"><svg viewBox="0 0 24 24"><rect x="7" y="3" width="10" height="18" rx="2"/><line x1="11" y1="18" x2="13" y2="18"/></svg></span>905-218-5937</li>
      <li><span class="icon"><svg viewBox="0 0 24 24"><path d="M5 4h4l2 5-2.5 1.5a11 11 0 0 0 5 5L15 13l5 2v4a2 2 0 0 1-2 2A16 16 0 0 1 3 6a2 2 0 0 1 2-2z"/></svg></span>905-218-5937</li>
      <li><span class="icon"><svg viewBox="0 0 24 24"><rect x="3" y="6" width="18" height="12" rx="1"/><polyline points="3,7 12,13 21,7"/></svg></span>info@holvaster-example.com</li>
    </ul>

    <div class="web-base"></div>
    <div class="web-band">www.holvaster-example.com</div>
    <span class="icon web-icon"><svg viewBox="0 0 24 24"><circle cx="12" cy="12" r="9"/><ellipse cx="12" cy="12" rx="4" ry="9"/><line x1="3" y1="12" x2="21" y2="12"/></svg></span>

    <div class="front-footbar"></div>
    <div class="front-footline"></div>
  </section>

</main>
</body>
</html>
```